Crimson Ledger.com is wanting to create a Facebook Ad to attract buyers to come to their website. We are wanting buyers to register for free and create an account on Crimson Ledger. com. We want to increase the number of buyers by posting an ad on Facebook groups. The buyer will click the link to our websites registration page.
https://www.crimsonledger.com/account/users/register

Semi Trucks
Semi Trailers
Construction Equipment
Farm Equipment
Trailers
ATV/UTV
Boats
RVs

```html
<!DOCTYPE html>
<html lang="en">
<head>
<meta charset="utf-8">
<title>Crimson Ledger – Facebook Ad</title>
<link href="https://fonts.googleapis.com/css2?family=Montserrat:wght@500;700;800;900&family=Roboto:wght@400;500&display=swap" rel="stylesheet">
<style>
  :root{
    --ink:#141414;
    --panel:#0d0d0d;
    --white:#ffffff;
    --orange:#e0581c;
    --orange-bright:#f26522;
    --paper:#f1f1f1;
    --paper-shade:#e2e2e2;
  }
  *{box-sizing:border-box;margin:0;padding:0}
  html,body{width:1200px;height:713px;overflow:hidden;background:var(--paper)}
  .ad{position:relative;width:1200px;height:713px;overflow:hidden;
      background:linear-gradient(180deg,var(--paper) 0%,#fafafa 55%,var(--paper-shade) 100%);
      font-family:"Montserrat",sans-serif}
  .truck-photo{position:absolute;left:515px;top:46px;width:685px;height:640px;
      border-radius:40px 0 0 40px;
      background:
        radial-gradient(ellipse 50% 50% at 80% 55%,rgba(138,142,147,.85),transparent 70%),
        radial-gradient(ellipse 40% 40% at 50% 45%,rgba(200,32,31,.75),transparent 70%),
        radial-gradient(ellipse 35% 18% at 55% 75%,rgba(233,138,30,.55),transparent 70%),
        linear-gradient(160deg,#ececec 0%,#d9d9d9 100%)}
  .info-panel{position:absolute;left:0;top:0;width:377px;height:713px;background:var(--panel);color:var(--white)}
  .headline{position:absolute;left:36px;top:168px;font-weight:900;font-size:37px;line-height:53px;letter-spacing:.3px;text-transform:uppercase;white-space:nowrap}
  .tagline{position:absolute;left:40px;top:334px;font-family:"Roboto",sans-serif;font-size:25px;line-height:36px;font-weight:400}
  .tagline em{font-style:normal;color:var(--orange-bright);font-weight:500}
  .register{position:absolute;left:66px;top:482px;display:flex;align-items:center;
      height:44px;width:222px;border-radius:22px;background:var(--orange);padding-left:16px;
      color:var(--white);font-weight:700;font-size:16px;letter-spacing:.5px;text-decoration:none}
  .register-arrow{position:absolute;right:-6px;top:-5px;width:54px;height:54px;border-radius:50%;
      background:var(--white);display:flex;align-items:center;justify-content:center}
  .contact{position:absolute;left:66px;top:610px;display:flex;align-items:center;gap:10px}
  .contact-icon{width:40px;height:40px;border-radius:50%;background:var(--orange);display:flex;align-items:center;justify-content:center}
  .contact-label{font-weight:700;font-size:15px;letter-spacing:.5px}
  .contact-number{font-weight:700;font-size:25px;line-height:1.05}
  .pointer{position:absolute;left:336px;top:376px}
  .brand{position:absolute;left:430px;top:78px;display:flex;align-items:center;gap:14px}
  .brand-mark{width:34px;height:34px;background:var(--orange)}
  .brand-name{font-weight:900;font-size:38px;line-height:44px;color:var(--ink);letter-spacing:.5px}
  .search-pill{position:absolute;left:966px;top:646px;display:flex;align-items:center;
      height:42px;width:214px;border-radius:21px;background:var(--orange);padding-left:16px;
      color:var(--white);font-family:"Roboto",sans-serif;font-size:14px}
  .search-pill .search-btn{position:absolute;right:2px;top:2px;width:58px;height:38px;border-radius:19px;
      background:var(--white);display:flex;align-items:center;justify-content:center}
</style>
</head>
<body>
<main class="ad">
  <div class="truck-photo" role="img" aria-label="Row of red, orange and silver semi truck cabs lined up at an angle"></div>

  <section class="info-panel">
    <h1 class="headline">Connecting<br>Salvage<br>to Solutions</h1>
    <p class="tagline">Your <em>Trusted Heavy<br>Truck</em> Auction Site</p>
    <a class="register" href="https://www.crimsonledger.com/account/users/register">REGISTER NOW
      <span class="register-arrow">
        <svg width="40" height="40" viewBox="0 0 40 40"><circle cx="20" cy="20" r="18" fill="#141414"/><path d="M17 12l8 8-8 8" stroke="#fff" stroke-width="3.5" fill="none" stroke-linecap="round" stroke-linejoin="round"/></svg>
      </span>
    </a>
    <div class="contact">
      <span class="contact-icon">
        <svg width="22" height="22" viewBox="0 0 24 24"><path fill="#fff" d="M6.6 10.8a15.1 15.1 0 0 0 6.6 6.6l2.2-2.2a1 1 0 0 1 1-.25 11.4 11.4 0 0 0 3.6.57 1 1 0 0 1 1 1V20a1 1 0 0 1-1 1A17 17 0 0 1 3 4a1 1 0 0 1 1-1h3.5a1 1 0 0 1 1 1c0 1.25.2 2.45.57 3.57a1 1 0 0 1-.25 1z"/></svg>
      </span>
      <div>
        <div class="contact-label">MORE INFO</div>
        <div class="contact-number">+555-214-3390</div>
      </div>
    </div>
  </section>

  <svg class="pointer" width="151" height="171" viewBox="0 0 151 171"><polygon points="0,0 151,85.5 0,171" fill="#e0581c"/></svg>

  <div class="brand">
    <span class="brand-mark"></span>
    <span class="brand-name">CRIMSON<br>LEDGER</span>
  </div>

  <div class="search-pill">Your Brand Name
    <span class="search-btn">
      <svg width="22" height="22" viewBox="0 0 24 24"><circle cx="10" cy="10" r="6.5" stroke="#141414" stroke-width="2.8" fill="none"/><path d="M15 15l6 6" stroke="#141414" stroke-width="3" stroke-linecap="round"/></svg>
    </span>
  </div>
</main>
</body>
</html>
```